Event flyer for Sunday night Youth Group

Need a 4 x 6 or 5 x 7 flyer for a new youth group starting on April 14. The youth group is for students in middle school and high school so it needs to look fun and cool, but not childish. I prefer it not to include pictures of people unless it's so obscure you can't really see their faces. I've uploaded some pictures of flyers I like. I've also attached a couple versions of our logo to use on the flyer.
Information the flyer needs to include:
Youth Group
Sundays, 6-8pm (beginning April 14)
Location: Merriwick's - 4219 Hollowfern Ln S, Alderbrook, 97418
There will be dinner, games, friends, and a message.
Target Market(s)
Youth ages 13-18
Industry/Entity Type
Church
Colors
Designer to choose colors to be used in the design.
Look and feel

```html
<!DOCTYPE html>
<html lang="en">
<head>
<meta charset="utf-8">
<title>Youth Group Flyer</title>
<link href="https://fonts.googleapis.com/css2?family=Montserrat:wght@400;500;700;800;900&family=Poppins:wght@500&display=swap" rel="stylesheet">
<style>
  :root {
    --page: #ffffff;
    --night: #140a3a;
    --indigo: #2a0ea0;
    --violet: #7a1fd0;
    --magenta: #e01bb8;
    --hot-pink: #ff2fd0;
    --ink-dark: #0f0730;
    --gold-light: #fff3e6;
    --gold: #f0c9a6;
    --cream: #f7d49b;
    --cyan: #45d4f5;
    --white: #ffffff;
  }
  * { margin: 0; padding: 0; box-sizing: border-box; }
  html, body { width: 889px; height: 1200px; overflow: hidden; background: var(--page); }
  .flyer {
    position: absolute; left: 76px; top: 47px; width: 738px; height: 1107px;
    overflow: hidden; background: var(--ink-dark);
    font-family: "Montserrat", sans-serif; color: var(--white); text-align: center;
  }
  .crowd-backdrop {
    position: absolute; left: 0; top: 0; width: 100%; height: 920px;
    background:
      radial-gradient(ellipse at 50% 78%, rgba(255,60,220,.55), transparent 60%),
      linear-gradient(180deg, #1a0a8a 0%, #3a10b0 30%, #7a1fd0 50%, #c41ac8 68%, #e01bb8 85%, #b0149e 100%);
  }
  .brand-mark {
    position: absolute; left: 50%; top: 78px; width: 84px; height: 84px; margin-left: -42px;
    border-radius: 50%; background: var(--white); box-shadow: 0 0 24px rgba(255,255,255,.5);
  }
  .brand-name {
    position: absolute; width: 100%; font-weight: 500; color: var(--white); line-height: 1;
  }
  .brand-name-main { top: 228px; font-size: 46px; letter-spacing: 1px; }
  .brand-name-sub { top: 276px; font-size: 26px; letter-spacing: 10px; padding-left: 10px; }
  .title {
    position: absolute; width: 100%; font-weight: 800; font-size: 176px; line-height: 1;
    letter-spacing: -3px;
    background: linear-gradient(180deg, var(--gold-light) 0%, var(--gold) 55%, #fbe4d0 100%);
    -webkit-background-clip: text; background-clip: text; color: transparent;
    filter: drop-shadow(0 4px 4px rgba(60,0,60,.45));
  }
  .title-youth { top: 312px; }
  .title-group { top: 453px; left: 8px; }
  .rule {
    position: absolute; left: 90px; width: 558px; height: 2px;
    background: linear-gradient(90deg, transparent, rgba(255,255,255,.85), transparent);
  }
  .rule-top { top: 620px; }
  .rule-bottom { top: 774px; }
  .schedule-day { position: absolute; top: 636px; width: 100%; font-weight: 800; font-size: 56px; line-height: 1; }
  .schedule-time {
    position: absolute; top: 684px; width: 100%; font-weight: 800; font-size: 86px; line-height: 1;
    letter-spacing: -2px;
    background: linear-gradient(180deg, var(--gold-light), var(--gold));
    -webkit-background-clip: text; background-clip: text; color: transparent;
  }
  .start-date-strip { position: absolute; left: 98px; top: 800px; width: 548px; height: 56px; }
  .start-date {
    position: absolute; top: 808px; width: 100%; font-weight: 800; font-size: 38px; line-height: 1.1;
    color: var(--magenta);
  }
  .torn-edge { position: absolute; left: 0; top: 885px; width: 738px; height: 50px; }
  .features-band {
    position: absolute; left: 0; top: 967px; width: 100%; height: 42px;
    background: linear-gradient(180deg, #5a1480, #a01a9c);
    border-bottom: 3px solid var(--hot-pink);
    font-weight: 800; font-size: 25px; letter-spacing: 3px; line-height: 42px; color: var(--cream);
  }
  .address {
    position: absolute; top: 1036px; width: 100%;
    font-family: "Poppins", sans-serif; font-weight: 500; font-size: 19px; line-height: 28px;
    display: flex; justify-content: center; align-items: center; gap: 10px;
  }
  .pin { width: 24px; height: 34px; }
</style>
</head>
<body>
  <main class="flyer">
    <div class="crowd-backdrop" role="img" aria-label="Purple and magenta haze over a blurred crowd with raised hands, faces not visible"></div>

    <div class="brand-mark"></div>
    <div class="brand-name brand-name-main">WAYFARER</div>
    <div class="brand-name brand-name-sub">FELLOWSHIP</div>

    <h1 class="title title-youth">YOUTH</h1>
    <div class="title title-group">GROUP</div>

    <div class="rule rule-top"></div>
    <div class="schedule-day">SUNDAYS</div>
    <div class="schedule-time">6-8PM</div>
    <div class="rule rule-bottom"></div>

    <svg class="start-date-strip" viewBox="0 0 548 56" preserveAspectRatio="none" aria-hidden="true">
      <path d="M40 6 L530 2 L520 12 L548 14 L500 22 L540 30 L470 38 L548 44 L300 52 L0 54 L60 44 L20 36 L70 28 L10 20 L60 12 Z" fill="#ffffff"/>
    </svg>
    <div class="start-date">APRIL 14, 2024</div>

    <svg class="torn-edge" viewBox="0 0 738 50" preserveAspectRatio="none" aria-hidden="true">
      <path d="M0 8 L40 12 L80 6 L130 14 L180 10 L230 16 L280 8 L330 12 L380 4 L430 10 L480 6 L540 14 L600 8 L660 12 L700 6 L738 10 L738 50 L0 50 Z" fill="#45d4f5"/>
      <path d="M0 20 L50 24 L90 18 L140 28 L200 22 L250 26 L300 20 L350 24 L400 16 L450 22 L500 20 L560 28 L620 22 L680 30 L738 34 L738 50 L0 50 Z" fill="#0f0730"/>
    </svg>

    <div class="features-band">DINNER • GAMES • FRIENDS • A MESSAGE</div>

    <div class="address">
      <svg class="pin" viewBox="0 0 24 34" aria-hidden="true">
        <path d="M12 0 C5 0 0 5 0 12 C0 21 12 34 12 34 C12 34 24 21 24 12 C24 5 19 0 12 0 Z M12 7 A5 5 0 1 1 12 17 A5 5 0 1 1 12 7 Z" fill="#ffffff" fill-rule="evenodd"/>
      </svg>
      <span>MERRIWICK'S – 4219 HOLLOWFERN LN S, ALDERBROOK, 97418</span>
    </div>
  </main>
</body>
</html>
```